design a web site for Vantrel Cable Works

Require a web site for a new business. We design, implement and manage high level and highly secure IT solutions for high end corporates and large government departments. we specialize in Secure Fibre optic products for highly secure LAN environments and data centre expertise

Target Market(s)

High end corporates and large government departments

Industry/Entity Type

IT

Coding

Coded - Design and coding required

Number of Pages Required

5+ page

Font styles to use
Other font styles liked:
• Calibri

Colors
0054AA
0677BA
7BADD7
CADEEF
E8F1F8
EB3D1F
EC4F4E
F09395
F8D3D4
FCEDEE

Requirements
Must have
• High end tech look and feel needs to incorporate the VCW Company Logo Three major sections. Basic all day Fibre solutions for everyone. High end solutions for blue chip customers. And high secure solutions for sensitive customers
Nice to have
• Online catalogue
Should not have
• Mundane or outdated look and feel

```html
<!DOCTYPE html>
<html lang="en">
<head>
<meta charset="utf-8">
<title>Vantrel Cable Works</title>
<link href="https://fonts.googleapis.com/css2?family=Michroma&family=PT+Sans+Narrow:wght@400;700&family=Poppins:wght@400;500;600&display=swap" rel="stylesheet">
<style>
:root{
  --red:#B5192B;
  --navy:#0E1E5B;
  --navy-deep:#0B1A4E;
  --grey-bg:#F5F4F6;
  --grey-slant:#CED3DE;
  --text:#2B2B2B;
  --muted:#BDBDBD;
  --white:#FFFFFF;
}
*{box-sizing:border-box;margin:0;padding:0}
html,body{width:1200px;height:2707px;overflow:hidden}
body{position:relative;background:var(--white);font-family:"PT Sans Narrow",sans-serif;color:var(--text)}
.abs{position:absolute}
.display{font-family:"Michroma",sans-serif}
.btn{position:absolute;background:var(--red);color:var(--white);border-radius:22px;font-size:18px;display:flex;align-items:center;justify-content:center}

/* header */
.site-header{left:0;top:0;width:1200px;height:104px;background:var(--red)}
.brand{left:140px;top:22px;display:flex;align-items:center;gap:8px;color:var(--white);font-size:18px;font-weight:700;letter-spacing:.5px}
.brand-mark{width:40px;height:40px;background:var(--navy)}
.brand-sub{position:absolute;left:48px;top:34px;font-size:11px;letter-spacing:3px;font-weight:400;white-space:nowrap}
.main-nav a{position:absolute;top:42px;color:var(--white);font-size:18px;text-decoration:none}
.login{left:947px;top:35px;width:131px;height:40px;background:var(--navy-deep);color:var(--white);border-radius:20px;font-size:18px;display:flex;align-items:center;justify-content:center}

/* hero */
.hero{left:0;top:104px;width:1200px;height:512px;background:radial-gradient(ellipse at 60% 70%,#2D5B9A 0%,#163A74 35%,#0C2352 75%,#0A1A3F 100%)}
.hero-cut{left:0;top:470px;width:1200px;height:150px}
.hero-copy{left:0;top:202px;width:1200px;text-align:center;color:var(--white)}
.hero-kicker{font-size:21px}
.hero-title{font-size:42px;margin-top:4px;letter-spacing:-1px}
.hero-lead{font-size:18px;line-height:26px;margin:14px auto 0;width:540px;font-family:"PT Sans Narrow",sans-serif}

/* partners */
.partner{top:666px;width:140px;height:122px;display:flex;flex-direction:column;align-items:center;gap:14px}
.partner .disc{width:70px;height:70px;border-radius:50%;background:#D6D6D6}
.partner .bar{width:140px;height:18px;background:#DDDDDD;border-radius:3px}

/* about */
.about-photo{left:120px;top:885px;width:387px;height:209px;background:linear-gradient(110deg,#5B4E3E,#2C3447 45%,#B08456 100%);border-radius:6px}
.about-block{left:89px;top:940px;width:194px;height:182px;background:var(--red);border-radius:6px}
.section-title{color:var(--navy);font-size:31px}
.about-text{left:560px;top:944px;width:520px;font-size:17.5px;line-height:27px}

/* services band */
.services-band{left:0;top:1214px;width:1200px;height:594px;background:var(--grey-bg)}
.service-card{top:1288px;width:322px;height:138px}
.service-card.active{left:128px;background:var(--navy);border-radius:4px;color:var(--white)}
.service-label{position:absolute;font-family:"Michroma",sans-serif;font-size:15.5px;line-height:27px;letter-spacing:-.5px}
.divider{width:1px;background:#D8D8D8;top:1300px;height:120px}
.fusion-photo{left:137px;top:1515px;width:315px;height:172px;background:linear-gradient(120deg,#7A6A50,#3B3F48 50%,#D8B441 100%);border-radius:6px}
.fusion-block{left:112px;top:1562px;width:158px;height:147px;background:var(--red);border-radius:6px}
.fusion-text{left:491px;top:1513px;width:585px;font-size:17.5px;line-height:27.3px;text-align:justify}

/* testimonials */
.testimonials{left:0;top:1808px;width:1200px;height:283px;background:var(--navy)}
.t-head{left:0;top:1850px;width:1200px;text-align:center;color:var(--white)}
.t-head h2{font-family:"Michroma",sans-serif;font-size:26px;font-weight:400;letter-spacing:-1px}
.t-head p{font-family:"Poppins",sans-serif;font-weight:500;font-size:15.5px;margin-top:12px}
.t-card{top:1975px;width:278px;height:285px;background:var(--white);box-shadow:0 4px 14px rgba(0,0,0,.08)}
.t-card .quote{position:absolute;left:18px;top:-14px}
.t-card p{position:absolute;left:18px;top:54px;width:244px;font-family:"Poppins",sans-serif;font-size:10.5px;line-height:20px;text-align:justify;color:#333}
.t-card .stars{position:absolute;left:86px;top:192px}
.t-card .name{position:absolute;width:100%;top:226px;text-align:center;font-size:18px;font-weight:700}
.t-card .place{position:absolute;width:100%;top:253px;text-align:center;font-size:17px}
.t-card .tail{position:absolute;right:60px;bottom:-20px}
.arrow{top:2096px}

/* footer */
.footer-bg{left:0;top:2333px;width:1200px;height:374px;background:var(--grey-bg)}
.footer-brand{left:138px;top:2440px;width:180px;text-align:center;color:var(--navy)}
.footer-brand .mark{width:44px;height:44px;background:var(--navy);margin:0 auto 8px}
.footer-brand .name{font-size:17px;font-weight:700;letter-spacing:.5px}
.footer-brand .sub{font-size:10px;letter-spacing:3px;color:var(--red)}
.footer-nav{left:375px;top:2436px;width:705px;height:32px;background:var(--red);display:flex;align-items:center;padding-left:130px;gap:0}
.footer-nav a{color:var(--white);font-size:18px;text-decoration:none;width:130px}
.footer-text{left:377px;top:2484px;width:705px;font-family:"Poppins",sans-serif;font-size:13.5px;line-height:27px;text-align:justify}
.social{top:2556px;width:15px;height:15px;border-radius:50%;background:#111}
.contact{top:2598px;display:flex;align-items:center;gap:8px;font-family:"Poppins",sans-serif;font-size:12.5px}
.contact .ico{width:24px;height:24px;border-radius:50%;background:var(--red);display:flex;align-items:center;justify-content:center}
.footer-rule{left:0;top:2641px;width:1200px;height:1px;background:#DADADA}
.copyright{left:0;top:2666px;width:1200px;text-align:center;font-family:"Poppins",sans-serif;font-size:12px}
</style>
</head>
<body>

<header class="site-header abs">
  <div class="brand abs"><span class="brand-mark"></span>VANTREL CABLE WORKS<span class="brand-sub">VCW</span></div>
  <nav class="main-nav">
    <a style="left:559px;font-weight:700">Home</a>
    <a style="left:643px">About Us</a>
    <a style="left:746px">Services</a>
    <a style="left:843px">Contact</a>
  </nav>
  <a class="login abs">Login / Signup</a>
</header>

<section class="hero abs" role="img" aria-label="Night city skyline with glowing network connection lines"></section>
<svg class="hero-cut abs" viewBox="0 470 1200 150" width="1200" height="150">
  <polygon points="0,616 600,548 1200,616 1200,620 0,620" fill="#FFFFFF"/>
  <polygon points="600,548 1200,483 1200,616" fill="#B5192B"/>
</svg>
<div class="hero-copy abs">
  <div class="hero-kicker display">WELCOME TO</div>
  <div class="hero-title display">VANTREL CABLE WORKS</div>
  <p class="hero-lead">"Lorem ipsum dolor sit amet, consectetur adipiscing elit, sed do eiusmod tempor incididunt ut labore et dolore magna aliqua.</p>
</div>
<a class="btn" style="left:527px;top:360px;width:142px;height:38px">Get Started</a>

<div class="partner abs" style="left:131px"><span class="disc"></span><span class="bar"></span></div>
<div class="partner abs" style="left:354px"><span class="disc"></span><span class="bar"></span></div>
<div class="partner abs" style="left:572px"><span class="disc"></span><span class="bar"></span></div>
<div class="partner abs" style="left:771px"><span class="disc"></span><span class="bar"></span></div>
<div class="partner abs" style="left:952px"><span class="disc"></span><span class="bar"></span></div>

<div class="about-block abs"></div>
<div class="about-photo abs" role="img" aria-label="Business team reviewing a tablet in an office"></div>
<h2 class="section-title display abs" style="left:560px;top:888px;font-weight:400">ABOUT US</h2>
<p class="about-text abs">Lorem ipsum dolor sit amet, consectetur adipiscing elit, sed do eiusmod tempor incididunt ut labore et dolore magna aliqua. Quis ipsum suspendisse ultrices gravida. Risus commodo viverra maecenas accumsan lacus vel facilisis.</p>
<a class="btn" style="left:558px;top:1072px;width:143px;height:40px">Read More</a>

<section class="services-band abs"></section>
<div class="service-card active abs">
  <svg class="abs" style="left:14px;top:14px" width="52" height="52" viewBox="0 0 52 52">
    <path d="M26 6a20 20 0 1 1-17 30" fill="none" stroke="#fff" stroke-width="7"/>
    <polygon points="40,40 52,44 42,52" fill="#fff"/>
    <text x="0" y="50" font-family="Michroma,sans-serif" font-size="12" fill="#fff" font-weight="700">ALL</text>
  </svg>
  <div class="service-label" style="left:14px;top:74px">BASIC ALL-DAY FIBRE<br>SOLUTIONS FOR EVERYONE.</div>
</div>
<div class="divider abs" style="left:472px"></div>
<svg class="abs" style="left:488px;top:1290px" width="70" height="66" viewBox="0 0 70 66" fill="none" stroke="#B5192B" stroke-width="2">
  <circle cx="35" cy="24" r="16"/><circle cx="35" cy="24" r="6"/>
  <path d="M28 40v20M42 40v20M12 10l6 5M58 10l-6 5M35 0v6"/>
</svg>
<div class="service-label abs" style="left:490px;top:1367px;color:#1A1A1A">HIGH-END SOLUTIONS FOR<br>BLUE CHIP CUSTOMERS.</div>
<div class="divider abs" style="left:810px"></div>
<svg class="abs" style="left:834px;top:1292px" width="56" height="56" viewBox="0 0 56 56" fill="none" stroke="#B5192B" stroke-width="2">
  <circle cx="28" cy="28" r="25"/>
  <rect x="17" y="26" width="22" height="18" rx="2"/>
  <path d="M21 26v-6a7 7 0 0 1 14 0v6"/><circle cx="28" cy="34" r="2.5"/>
</svg>
<div class="service-label abs" style="left:830px;top:1367px;color:#1A1A1A">HIGH-SECURE SOLUTIONS<br>FOR SENSITIVE CUSTOMERS</div>

<div class="fusion-block abs"></div>
<div class="fusion-photo abs" role="img" aria-label="Technician hands operating a fibre fusion splicer"></div>
<p class="fusion-text abs">Lorem ipsum dolor sit amet, consectetur adipiscing elit, sed do eiusmod tempor incididunt ut labore et dolore magna aliqua. Quis ipsum suspendisse ultrices gravida. Risus commodo viverra maecenas accumsan lacus vel facilisis. Lorem ipsum dolor sit amet, consectetur adipiscing elit, sed do eiusmod tempor incididunt ut labore et dolore magna aliqua. Quis ipsum suspendisse ultrices gravida. Risus commodo viverra maecenas accumsan lacus vel facilisis.</p>
<a class="btn" style="left:489px;top:1695px;width:143px;height:40px">Read More</a>

<section class="testimonials abs"></section>
<div class="t-head abs">
  <h2>TESTIMONIALS</h2>
  <p>Lorem ipsum dolor sit amet, consectetur adipiscing elit, sed do eiusmod tempor incididunt ut labore et dolore magna aliqua.</p>
</div>

<svg class="arrow abs" style="left:103px" width="16" height="24" viewBox="0 0 16 24"><path d="M13 2L3 12l10 10" fill="none" stroke="#111" stroke-width="3"/></svg>
<svg class="arrow abs" style="left:1078px" width="16" height="24" viewBox="0 0 16 24"><path d="M3 2l10 10L3 22" fill="none" stroke="#111" stroke-width="3"/></svg>

<div class="t-card abs" style="left:145px">
  <svg class="quote" width="56" height="46" viewBox="0 0 56 46" fill="#B5192B"><path d="M0 18Q2 2 20 0v8Q10 10 10 18h14v28H0zM30 18Q32 2 50 0v8Q40 10 40 18h14v28H30z"/></svg>
  <p>Lorem ipsum dolor sit amet, consectetur adipiscing elit, sed do eiusmod tempor incididunt ut labore et dolore magna aliqua. Ut enim ad minim veniam, quis nostrud exercitation ullamco laboris nisi ut aliquip ex ea commodo consequat. Duis aute irure dolor in reprehenderit in voluptate</p>
  <svg class="stars" width="108" height="20" viewBox="0 0 108 20" fill="#B5192B"><g id="s"><polygon points="10,0 12.9,6.9 20,7.3 14.5,12 16.2,19 10,15.2 3.8,19 5.5,12 0,7.3 7.1,6.9"/></g><use href="#s" x="22"/><use href="#s" x="44"/><use href="#s" x="66"/><use href="#s" x="88"/></svg>
  <div class="name">Dana Whitlow</div><div class="place">USA</div>
  <svg class="tail" width="24" height="20" viewBox="0 0 24 20"><polygon points="0,0 24,0 0,20" fill="#fff"/></svg>
</div>
<div class="t-card abs" style="left:462px">
  <svg class="quote" width="56" height="46" viewBox="0 0 56 46" fill="#B5192B"><path d="M0 18Q2 2 20 0v8Q10 10 10 18h14v28H0zM30 18Q32 2 50 0v8Q40 10 40 18h14v28H30z"/></svg>
  <p>Lorem ipsum dolor sit amet, consectetur adipiscing elit, sed do eiusmod tempor incididunt ut labore et dolore magna aliqua. Ut enim ad minim veniam, quis nostrud exercitation ullamco laboris nisi ut aliquip ex ea commodo consequat. Duis aute irure dolor in reprehenderit in voluptate</p>
  <svg class="stars" width="108" height="20" viewBox="0 0 108 20" fill="#B5192B"><use href="#s"/><use href="#s" x="22"/><use href="#s" x="44"/><use href="#s" x="66"/><use href="#s" x="88"/></svg>
  <div class="name">Dana Whitlow</div><div class="place">USA</div>
  <svg class="tail" width="24" height="20" viewBox="0 0 24 20"><polygon points="0,0 24,0 0,20" fill="#fff"/></svg>
</div>
<div class="t-card abs" style="left:779px">
  <svg class="quote" width="56" height="46" viewBox="0 0 56 46" fill="#B5192B"><path d="M0 18Q2 2 20 0v8Q10 10 10 18h14v28H0zM30 18Q32 2 50 0v8Q40 10 40 18h14v28H30z"/></svg>
  <p>Lorem ipsum dolor sit amet, consectetur adipiscing elit, sed do eiusmod tempor incididunt ut labore et dolore magna aliqua. Ut enim ad minim veniam, quis nostrud exercitation ullamco laboris nisi ut aliquip ex ea commodo consequat. Duis aute irure dolor in reprehenderit in voluptate</p>
  <svg class="stars" width="108" height="20" viewBox="0 0 108 20" fill="#B5192B"><use href="#s"/><use href="#s" x="22"/><use href="#s" x="44"/><use href="#s" x="66"/><use href="#s" x="88"/></svg>
  <div class="name">Dana Whitlow</div><div class="place">USA</div>
  <svg class="tail" width="24" height="20" viewBox="0 0 24 20"><polygon points="0,0 24,0 0,20" fill="#fff"/></svg>
</div>

<footer>
  <svg class="abs" style="left:0;top:2330px" width="1200" height="377" viewBox="0 2330 1200 377">
    <polygon points="0,2333 600,2378 1200,2333 1200,2707 0,2707" fill="#F5F4F6"/>
    <polygon points="0,2333 600,2378 0,2420" fill="#CED3DE"/>
  </svg>
  <div class="footer-brand abs">
    <div class="mark"></div>
    <div class="name">VANTREL CABLE WORKS</div>
    <div class="sub">VCW</div>
  </div>
  <nav class="footer-nav abs">
    <a>Home</a><a>About Us</a><a>Service</a><a>Contact</a>
  </nav>
  <p class="footer-text abs">Lorem Ipsum is simply dummy text of the printing and typesetting industry. Lorem Ipsum has been the industry's standard dummy text ever since the 1500.</p>
  <span class="social abs" style="left:556px" aria-label="Social profile"></span>
  <span class="social abs" style="left:590px" aria-label="Social profile"></span>
  <span class="social abs" style="left:624px" aria-label="Social profile"></span>
  <div class="contact abs" style="left:253px">
    <span class="ico"><svg width="12" height="12" viewBox="0 0 12 12"><path d="M2 1l2 0 1 3-1.5 1a6 6 0 0 0 3 3L7.5 7l3 1v2Q10 11 8 11A7 7 0 0 1 1 4Q1 2 2 1z" fill="#fff"/></svg></span>+1 555 014-2290
  </div>
  <div class="contact abs" style="left:449px">
    <span class="ico"><svg width="12" height="10" viewBox="0 0 12 10"><rect x="0" y="0" width="12" height="10" rx="1" fill="#fff"/><path d="M0 1l6 4 6-4" fill="none" stroke="#B5192B" stroke-width="1.2"/></svg></span>info@vantrelcable.com
  </div>
  <div class="contact abs" style="left:683px">
    <span class="ico"><svg width="10" height="13" viewBox="0 0 10 13"><path d="M5 0a5 5 0 0 1 5 5c0 3-5 8-5 8S0 8 0 5a5 5 0 0 1 5-5z" fill="#fff"/><circle cx="5" cy="5" r="1.8" fill="#B5192B"/></svg></span># 212, Harlow Street, city, USA - 5486
  </div>
  <div class="footer-rule abs"></div>
  <p class="copyright abs">© copyrights 2022 Vantrel Cable Works |&nbsp; All Rights Reserved</p>
</footer>

</body>
</html>
```